Halvorsen Construction Needs a Business Card

Our current business card is very bland, and since we have a new logo, we would like a new business card design to reflect our company. It can be a single-sided or two-sided card, but it is important that our contact information appears on the same side. I am attaching a copy of our old card and our new logo. If you need the logo in another format than the one I'm sending, please let me know. This is the information that we must have on our card, but not necessarily in any specific order:
1) Our logo
2) General Contractor
3) Dale Halvorsen, Owner
4) 482 Commerce Ridge Road, Centre, Alabama 35871
5) Office: 256-555-0147
7) Fax: 256-555-0148
8) Cell: 256-555-0193
9) halvorsenconstruction@qvl-mail.net
10) halvorsenconstruction-example.com (can be omitted if necessary)
Also, I will need files in a format that I can alter if any of the above information changes in the near future. Thank you in advance for your submissions!
Target Market(s)
Commercial and residential clients, architects, and subcontractors.
Industry/Entity Type
Business
Look and feel

```html
<!DOCTYPE html>
<html lang="en">
<head>
<meta charset="utf-8">
<title>Halvorsen Construction – Business Card</title>
<link rel="stylesheet" href="https://fonts.googleapis.com/css2?family=EB+Garamond:ital,wght@0,400;0,600;0,700;1,700&display=swap">
<style>
  :root {
    --ink: #231f20;
    --paper: #ffffff;
    --band: #fdc93e;
    --frame: #231f20;
  }
  * { margin: 0; padding: 0; box-sizing: border-box; }
  html, body {
    width: 1200px;
    height: 686px;
    overflow: hidden;
    background: var(--paper);
  }
  .card {
    position: relative;
    width: 1200px;
    height: 686px;
    background: var(--paper);
    border: 21px solid var(--frame);
    font-family: "EB Garamond", Georgia, serif;
    color: var(--ink);
  }
  .brand {
    position: absolute;
    left: 102px;
    top: 36px;
    height: 188px;
    display: flex;
    align-items: center;
    gap: 40px;
  }
  .brand-square {
    width: 188px;
    height: 188px;
    background: var(--ink);
    flex: none;
  }
  .brand-name {
    font-size: 62px;
    font-weight: 600;
    line-height: 1;
    color: var(--ink);
    white-space: nowrap;
  }
  .title-band {
    position: absolute;
    left: 0;
    right: 0;
    top: 267px;
    height: 110px;
    background: var(--band);
    padding: 3px 0 0 331px;
  }
  .title-band p {
    font-size: 42px;
    line-height: 54px;
  }
  .address {
    position: absolute;
    left: 67px;
    top: 439px;
    font-size: 34px;
    line-height: 38px;
  }
  .contact {
    position: absolute;
    left: 597px;
    top: 400px;
    font-size: 34px;
    line-height: 37px;
  }
  .contact .label {
    font-weight: 700;
    font-style: italic;
  }
  .contact .email {
    margin-top: 3px;
    font-size: 32px;
  }
  .website {
    position: absolute;
    left: 0;
    right: 0;
    top: 572px;
    text-align: center;
    font-size: 42px;
    font-weight: 700;
    line-height: 1;
  }
</style>
</head>
<body>
  <div class="card">
    <header class="brand">
      <div class="brand-square" aria-hidden="true"></div>
      <div class="brand-name">Halvorsen Construction</div>
    </header>

    <section class="title-band">
      <p class="role">General Contractor</p>
      <p class="person">Dale Halvorsen, Owner</p>
    </section>

    <address class="address" style="font-style: normal;">
      482 Commerce Ridge Road<br>
      Centre, Alabama 35871
    </address>

    <div class="contact">
      <p><span class="label">Office</span>: 256-555-0147</p>
      <p><span class="label">Fax</span>: 256-555-0148</p>
      <p><span class="label">Cell</span>: 256-555-0193</p>
      <p class="email">halvorsenconstruction@qvl-mail.net</p>
    </div>

    <p class="website">halvorsenconstruction-example.com</p>
  </div>
</body>
</html>
```